Design a Brochure for a Sign Company

Contest Brief
Required (finished product): AI file (CS5 only), PDF (Acrobat 9 or less), supply fonts used. All the copy should be vector format.
Attached: Copy for brochure. Use images from my website ([login to view URL]) and if needed I will supply images for the final product.

About My Company and Market
My company is an established sign company and my target market is other businesses and corporations. I'd like to let our products speak for themselves but be sure to use the information I've included. The Introduction and the Call to Action can be in any order if it helps the design - its up to you. The format and how you manipulate and revise the graphics is your call. All of these photos are photos of our work so there's no problem with ownership of the graphics. If you can't use my website photos let me know. Be as creative as you'd like.

```html
<!DOCTYPE html>
<html lang="en">
<head>
<meta charset="utf-8">
<title>Brightline Signworks Brochure</title>
<link rel="stylesheet" href="https://fonts.googleapis.com/css2?family=Arimo:wght@400;700&display=swap">
<style>
  :root {
    --backdrop: #e3e5e9;
    --paper: #ffffff;
    --royal: #1f35b8;
    --royal-deep: #0f1f8f;
    --navy-text: #1a2a9a;
    --aqua: #9fe3ef;
    --ink: #111111;
    --on-blue: #ffffff;
    --tick: #2a55c8;
  }
  * { box-sizing: border-box; margin: 0; padding: 0; }
  html, body { width: 1200px; height: 1200px; overflow: hidden; }
  body {
    background: var(--backdrop);
    font-family: "Arimo", Arial, sans-serif;
    color: var(--ink);
    position: relative;
  }
  .spread {
    position: absolute;
    left: 240px;
    width: 720px;
    height: 509px;
    background: var(--paper);
    overflow: hidden;
  }
  .spread--cover { top: 51px; }
  .spread--inside { top: 588px; }
  .spread__art { position: absolute; inset: 0; width: 720px; height: 509px; }
  .spread__copy { position: absolute; }

  .cover-title { font-weight: 400; line-height: 1.2; text-align: center; }
  .cover-title--back { left: 20px; top: 40px; width: 200px; font-size: 27px; color: var(--paper); }
  .cover-title--front { left: 380px; top: 108px; width: 310px; font-size: 32px; color: var(--navy-text); }

  .service-list { left: 20px; top: 256px; list-style: none; font-size: 12.5px; line-height: 1.25; }
  .service-list li { display: flex; align-items: flex-start; margin-bottom: 6px; }
  .service-list svg { flex: 0 0 12px; margin: 1px 8px 0 0; }
  .service-list .indent { display: block; padding-left: 46px; }

  .section-title { font-size: 17px; font-weight: 400; }
  .section-body { font-size: 12px; line-height: 1.2; }
  .section-body--justify { text-align: justify; font-size: 11.5px; line-height: 1.2; }
  .on-blue { color: var(--on-blue); }

  .intro-title { left: 16px; top: 30px; }
  .intro-body { left: 14px; top: 60px; width: 320px; }
  .ada-title { left: 19px; top: 184px; }
  .ada-body { left: 14px; top: 212px; width: 320px; }
  .letters-title { left: 19px; top: 370px; }
  .letters-body { left: 14px; top: 398px; width: 330px; }

  .carved-title { left: 399px; top: 20px; }
  .carved-body { left: 383px; top: 48px; width: 325px; }
  .sand-title { left: 383px; top: 230px; }
  .sand-body { left: 383px; top: 260px; width: 325px; }
  .way-title { left: 383px; top: 368px; width: 260px; text-align: center; line-height: 1.25; }
  .way-body { left: 383px; top: 418px; width: 325px; }
</style>
</head>
<body>

<section class="spread spread--cover" aria-label="Brochure cover">
  <svg class="spread__art" viewBox="0 0 720 509">
    <defs>
      <linearGradient id="fold-shade" x1="0" x2="1" y1="0" y2="0">
        <stop offset="0" stop-color="#cfd2d6"/>
        <stop offset="0.25" stop-color="#f4f4f5"/>
        <stop offset="1" stop-color="#ffffff"/>
      </linearGradient>
      <linearGradient id="band-blue" x1="0" x2="1" y1="0" y2="0">
        <stop offset="0" stop-color="#2238b9"/>
        <stop offset="1" stop-color="#1a2fa8"/>
      </linearGradient>
      <linearGradient id="restroom-tones" x1="0" x2="1">
        <stop offset="0" stop-color="#3a3a3e"/>
        <stop offset="0.5" stop-color="#e9e5b8"/>
        <stop offset="1" stop-color="#2a4fb0"/>
      </linearGradient>
      <linearGradient id="lobby-tones" x1="0" x2="0" y1="0" y2="1">
        <stop offset="0" stop-color="#d8d2a0"/>
        <stop offset="0.5" stop-color="#b8ae8a"/>
        <stop offset="1" stop-color="#8f8a80"/>
      </linearGradient>
    </defs>
    <rect x="360" y="0" width="360" height="509" fill="url(#fold-shade)"/>
    <path d="M0 0 H720 V150 C650 140 560 60 360 78 C220 92 120 150 0 152 Z" fill="url(#band-blue)" opacity="0.25"/>
    <path d="M0 162 C120 160 220 100 360 88 C560 70 650 150 720 160 V148 C650 138 560 58 360 76 C220 90 120 148 0 150 Z" fill="var(--aqua)"/>
    <path d="M0 0 H720 V140 C650 130 560 50 360 68 C220 82 120 138 0 140 Z" fill="url(#band-blue)"/>
    <circle cx="307" cy="300" r="97" fill="url(#restroom-tones)" role="img" aria-label="Photo of women and accessible restroom signs"/>
    <circle cx="576" cy="373" r="153" fill="url(#lobby-tones)" role="img" aria-label="Photo of dimensional lettering on a performing arts center lobby wall"/>
  </svg>

  <h1 class="spread__copy cover-title cover-title--back">Brightline<br>Signworks</h1>
  <h2 class="spread__copy cover-title cover-title--front">Brightline<br>Signworks</h2>

  <ul class="spread__copy service-list">
    <li><svg width="12" height="12" viewBox="0 0 12 12"><path d="M1 6 L4.5 9.5 L11 2" fill="none" stroke="var(--tick)" stroke-width="2"/></svg>Interior and ADA Signs</li>
    <li><svg width="12" height="12" viewBox="0 0 12 12"><path d="M1 6 L4.5 9.5 L11 2" fill="none" stroke="var(--tick)" stroke-width="2"/></svg>Dimensional Letters</li>
    <li><svg width="12" height="12" viewBox="0 0 12 12"><path d="M1 6 L4.5 9.5 L11 2" fill="none" stroke="var(--tick)" stroke-width="2"/></svg>Carved Signs</li>
    <li><svg width="12" height="12" viewBox="0 0 12 12"><path d="M1 6 L4.5 9.5 L11 2" fill="none" stroke="var(--tick)" stroke-width="2"/></svg>Sandblasted Signs</li>
    <li><svg width="12" height="12" viewBox="0 0 12 12"><path d="M1 6 L4.5 9.5 L11 2" fill="none" stroke="var(--tick)" stroke-width="2"/></svg><span>Wayfinding / Post and Panel<span class="indent">Systems</span></span></li>
    <li><svg width="12" height="12" viewBox="0 0 12 12"><path d="M1 6 L4.5 9.5 L11 2" fill="none" stroke="var(--tick)" stroke-width="2"/></svg>Event Signage</li>
    <li><svg width="12" height="12" viewBox="0 0 12 12"><path d="M1 6 L4.5 9.5 L11 2" fill="none" stroke="var(--tick)" stroke-width="2"/></svg>Call to Action</li>
  </ul>
</section>

<section class="spread spread--inside" aria-label="Brochure inside">
  <svg class="spread__art" viewBox="0 0 720 509" aria-hidden="true">
    <defs>
      <linearGradient id="inside-blue" x1="0" x2="1" y1="1" y2="0">
        <stop offset="0" stop-color="#1a2fb0"/>
        <stop offset="0.6" stop-color="#2a46c8"/>
        <stop offset="1" stop-color="#3a5ad8"/>
      </linearGradient>
      <linearGradient id="inside-fold" x1="0" x2="1">
        <stop offset="0" stop-color="#000" stop-opacity="0.18"/>
        <stop offset="1" stop-color="#000" stop-opacity="0"/>
      </linearGradient>
    </defs>
    <path d="M0 352 C220 352 330 350 355 300 C375 255 380 212 420 206 C520 200 640 200 720 198 V509 H0 Z" fill="var(--aqua)" transform="translate(0 -9)"/>
    <path d="M0 352 C220 352 330 350 355 300 C375 255 380 212 420 206 C520 200 640 200 720 198 V509 H0 Z" fill="url(#inside-blue)"/>
    <rect x="360" y="0" width="40" height="509" fill="url(#inside-fold)"/>
  </svg>

  <h3 class="spread__copy section-title intro-title">Introduction</h3>
  <p class="spread__copy section-body intro-body">Brightline Signworks is a provider of quality, custom commercial signage. We feature many varieties of signage — ADA compliant signage, dimensional letters, carved signs, sandblasted signs, event signage and more. Brightline Signworks can provide you with distinctive and unique signage that is crafted to your specifications, right here in the USA.</p>

  <h3 class="spread__copy section-title ada-title">Interior and ADA Signs</h3>
  <p class="spread__copy section-body ada-body">Matching existing signage? No problem! We are expert at reproduction of existing designs. Beyond that, we can work with you to custom design signage to fit your particular needs. We can also ensure ADA compliance where necessary. The Americans with Disabilities Act mandates that all public places have ADA-compliant signage. Let Brightline Signworks bring your signage into compliance and avoid steep fines.</p>

  <h3 class="spread__copy section-title on-blue letters-title">Dimensional Letters</h3>
  <p class="spread__copy section-body on-blue letters-body">Dimensional letters add distinction to entrances and reception areas and work equally well as exterior signage. We can supply cut and fabricated dimensional letters made from metals, plastics, wood and more. You can choose from a wide assortment of standard styles or we can accurately match any finish your project needs.</p>

  <h3 class="spread__copy section-title carved-title">Carved Signs</h3>
  <p class="spread__copy section-body section-body--justify carved-body">Our carved signs are built to withstand the elements. Meticulously crafted from either a highly durable PVC plastic material or a lightweight but still durable HDU material, each sign is then painted using a two-part acrylic paint finish, which comes with a five year warranty against fading. Color is no problem either. We can match any standard color or any paint swatch you supply. With our two-part acrylic paint system, your colors will stay vibrant for years. Carved signs are the perfect addition to businesses, retail locations, parking areas and more.</p>

  <h3 class="spread__copy section-title on-blue sand-title">Sandblasted Signs</h3>
  <p class="spread__copy section-body section-body--justify on-blue sand-body">Sandblasted signs have a unique look that adds distinction to any location. Made of HDU, a synthetic material that withstands all kinds of weather, water and insects, we can craft a sandblasted sign in any shape and then seal it with a resistant two-part acrylic finish which keeps colors crisp and comes with a five year guarantee on workmanship. We can match any standard color or paint swatch that you supply.</p>

  <h3 class="spread__copy section-title on-blue way-title">Wayfinding / Post and Panel<br>Systems</h3>
  <p class="spread__copy section-body section-body--justify on-blue way-body">Wayfinding signs help your visitors to find their way throughout your location. Brightline Signworks offers a variety of elegant sleek-finished aluminum signs, modular frames and panel systems featuring durable acrylic and weather-resistant PVC. We can provide clear and easy installation and service.</p>
</section>

</body>
</html>
```